Facebook Velarte9 to attract customers

We need a Facebook design that brings seriousness and professionalism in the field of business advice. We enclose the logo that a colleague of yours designed in Pixelmora.
The company is called: Velarte9 Asesoría y Administración de Empresas, but the commercial name is Velarte9.
We are dedicated to advising companies, providing the following services: tax, labor, accounting, administration and finance.
We would like a design that respects the colors of the attached logo, we also attach the logo in black and white, in case you need it for an image. The design, as we have already said, must communicate security, trust, professionalism and also be attractive for sale, that is, that customers who visit Facebook are attracted to ask for information, call, or give "like" in the page.
The client profile we are looking for are companies and freelancers.

Target Market(s)

Companies and freelancers in Spain

Industry/Entity Type

Asesoría de empresas, Consultoría

Font styles to use
Sans Serif

Colors
0054AA
0677BA
7BADD7
CADEEF
E8F1F8

Requirements
Must have
• We are a business consultancy so it must convey seriousness, professionalism, trust and that encourages being sold, that is, those who agree contact us or like the page
Nice to have
• Create a cover photo, that the services appear (Tax, Labor, Accounting, Administration and Financial), profile image (we have attached the logo if it is worth it), contact forms and access to quick likes. It is very important that it is compatible with the SEO and SEM of the company. We also seek to design a kind of "template" for our publications, making sure that each time we publish a format and an image are followed and we are recognized just by seeing the publication

```html
<!DOCTYPE html>
<html lang="es">
<head>
<meta charset="utf-8">
<title>Velarte9 – Portada de Facebook</title>
<link href="https://fonts.googleapis.com/css2?family=Montserrat:wght@500;600;700;800&display=swap" rel="stylesheet">
<style>
  :root {
    --navy: #0b2a8a;
    --brand-blue: #0054AA;
    --mid-blue: #0677BA;
    --sky: #1aa3e0;
    --light-blue: #7BADD7;
    --pale-blue: #CADEEF;
    --mist: #E8F1F8;
    --orange: #f7812d;
    --orange-deep: #f26a1b;
    --photo-dark: #0a1624;
    --photo-teal: #11405a;
    --white: #ffffff;
    --page: #eef1f5;
  }
  html, body {
    margin: 0;
    padding: 0;
    width: 1200px;
    height: 1022px;
    overflow: hidden;
    background: var(--page);
  }
  .canvas {
    position: relative;
    width: 1200px;
    height: 1022px;
  }
  .cover {
    position: absolute;
    left: 0;
    top: 288px;
    width: 1200px;
    height: 446px;
    display: block;
    font-family: "Montserrat", sans-serif;
  }
  .brand-name { font-weight: 700; font-size: 34px; fill: var(--white); letter-spacing: 0.5px; }
  .brand-tagline { font-weight: 600; font-size: 11.5px; fill: var(--white); letter-spacing: 0.4px; }
  .section-label { font-weight: 800; font-size: 18px; fill: var(--white); letter-spacing: 1.5px; }
  .service-name { font-weight: 700; font-size: 23px; fill: var(--white); }
  .contact-lead { font-weight: 600; font-size: 13px; fill: var(--white); }
  .contact-phone { font-weight: 800; font-size: 32px; fill: var(--white); }
  .contact-line { font-weight: 600; font-size: 22px; fill: var(--white); }
  .icon { fill: none; stroke: var(--white); stroke-width: 1.6; stroke-linecap: round; stroke-linejoin: round; }
</style>
</head>
<body>
<div class="canvas">
  <svg class="cover" viewBox="0 0 1200 446" xmlns="http://www.w3.org/2000/svg">
    <defs>
      <linearGradient id="panelBlue" x1="0" y1="0" x2="1" y2="0.3">
        <stop offset="0" stop-color="var(--navy)"/>
        <stop offset="0.55" stop-color="var(--mid-blue)"/>
        <stop offset="1" stop-color="var(--sky)"/>
      </linearGradient>
      <radialGradient id="photoTone" cx="0.6" cy="0.5" r="0.7">
        <stop offset="0" stop-color="var(--photo-teal)"/>
        <stop offset="1" stop-color="var(--photo-dark)"/>
      </radialGradient>
      <linearGradient id="orangeBand" x1="0" y1="0" x2="0" y2="1">
        <stop offset="0" stop-color="var(--orange)"/>
        <stop offset="1" stop-color="var(--orange-deep)"/>
      </linearGradient>
    </defs>

    <!-- Blue service panel -->
    <rect class="service-panel" x="0" y="0" width="1200" height="446" fill="url(#panelBlue)"/>

    <!-- Photo area -->
    <polygon class="photo-area" role="img" aria-label="Fotografía de un consultor con traje tocando un panel digital con iconos de finanzas y un gráfico de barras"
      points="700,0 1200,0 1200,446 905,446 905,330 700,170" fill="url(#photoTone)"/>

    <!-- Orange contact band -->
    <path class="contact-band" fill="url(#orangeBand)"
      d="M0,340 Q25,322 50,338 T100,338 T150,338 T200,338 T250,338 T300,338 T350,338 T400,338 T450,338 T500,338 T550,338 T600,338 L640,338 L905,446 L0,446 Z"/>

    <!-- Brand name -->
    <g class="brand">
      <rect x="42" y="26" width="38" height="38" rx="4" fill="var(--white)"/>
      <text class="brand-name" x="92" y="58">Velarte9</text>
      <text class="brand-tagline" x="92" y="80">ASESORÍA Y ADMINISTRACIÓN</text>
      <text class="brand-tagline" x="92" y="95">DE EMPRESAS</text>
    </g>

    <!-- Section label -->
    <g class="section-heading">
      <polygon points="42,127 352,127 368,160 42,160" fill="var(--navy)"/>
      <polygon points="42,127 190,127 206,160 42,160" fill="#0a2371"/>
      <line x1="206" y1="160" x2="420" y2="160" stroke="var(--navy)" stroke-width="2"/>
      <text class="section-label" x="56" y="151">SERVICIOS</text>
    </g>

    <!-- Services -->
    <g class="service-list">
      <g class="service">
        <rect class="icon" x="50" y="188" width="18" height="24" rx="2"/>
        <line class="icon" x1="54" y1="196" x2="64" y2="196"/><line class="icon" x1="54" y1="202" x2="64" y2="202"/>
        <text class="service-name" x="78" y="209">Impuesto</text>
      </g>
      <g class="service">
        <rect class="icon" x="240" y="188" width="22" height="26" rx="2"/>
        <rect class="icon" x="244" y="192" width="14" height="6"/>
        <line class="icon" x1="245" y1="204" x2="257" y2="204"/><line class="icon" x1="245" y1="209" x2="257" y2="209"/>
        <text class="service-name" x="272" y="211">Contabilidad</text>
      </g>
      <g class="service">
        <circle class="icon" cx="60" cy="244" r="6"/>
        <path class="icon" d="M48,264 Q60,248 72,264 Z"/>
        <text class="service-name" x="78" y="261">Labor</text>
      </g>
      <g class="service">
        <circle class="icon" cx="252" cy="244" r="6"/>
        <path class="icon" d="M240,264 Q252,248 264,264 Z"/>
        <circle class="icon" cx="262" cy="256" r="4"/>
        <text class="service-name" x="272" y="261">Administración</text>
      </g>
      <g class="service">
        <path class="icon" d="M54,290 L66,290 L70,296 Q76,312 60,314 Q44,312 50,296 Z"/>
        <text x="56" y="310" font-size="11" font-weight="700" fill="var(--white)">$</text>
        <text class="service-name" x="78" y="307">Financiero</text>
      </g>
    </g>

    <!-- Contact details -->
    <g class="contact">
      <text class="contact-lead" x="50" y="379">Llamanos Estimación gratuita</text>
      <path class="icon" d="M56,397 q-3,4 2,11 q6,7 11,4 l2,-3 l-5,-4 l-2,2 q-4,-2 -6,-6 l2,-2 l-3,-5 z" fill="var(--white)" stroke="none"/>
      <text class="contact-phone" x="76" y="418">622 418 305</text>
      <line x1="288" y1="362" x2="288" y2="420" stroke="var(--white)" stroke-width="1.5"/>
      <rect class="icon" x="304" y="380" width="16" height="11" rx="1"/>
      <polyline class="icon" points="304,380 312,387 320,380"/>
      <text class="contact-line" x="328" y="392">info@velarte9.com</text>
      <circle class="icon" cx="312" cy="413" r="8"/>
      <ellipse class="icon" cx="312" cy="413" rx="3.5" ry="8"/>
      <line class="icon" x1="304" y1="413" x2="320" y2="413"/>
      <text class="contact-line" x="328" y="421">www.velarte9.com</text>
    </g>
  </svg>
</div>
</body>
</html>
```